Due to client commitments, we don't have time in-house to complete this project...
We need a design refresh for our web company! It's time for us to move things along, so we're looking to PixelGuild to get this done!
Our clients tend to be associations and government, with some element of business clients. We need a design that appeals to this sophisticated target market.
Our current web site can be found at www.brindlecove.ca. We are looking for a more personable, contemporary look for the new site design. However, you can see our logo on this site, and some of the content.
The design you provide will be implemented in Nimbus. The design winner will only need to provide the PSD or Fireworks PNG format. We anticipate creating the template coding in-house.
However, if you have experience creating Nimbus templates, please let us know as we may ask you to bid separately to do that phase of the project.
We've provided you with wireframes of the home page and the inside page, along with Adobe Illustrator and PSD versions of our logo.
For the home page, we've indicated that we'd like to have a slider implemented into the design. For the purpose of design, we believe we'll use this slider: http://demo.tallowforge.com/breezy-fanfold-carousel.html.
The slider will contain inspiration photos related to each of the tabs. Ideally, we would like you to suggest the images for the slider. The dimension of the slider can be adjusted. We would like more space for the image with less for the text. The slider height should be sufficient to ensure the image "stimulates" the audience and sets the tone for the landing page.
The wireframe is provided to illustrate the placement of content and menu items. The exact dimensions of each component can be revised as you see fit.
Our clients tend to be associations, non-profit, government, and business clients. We need a design that appeals to this sophisticated target market.
Business

```html
<!DOCTYPE html>
<html lang="en">
<head>
<meta charset="utf-8">
<title>BrindleCove Communications</title>
<link rel="stylesheet" href="https://fonts.googleapis.com/css2?family=Arimo:wght@400;700&family=Tinos:wght@400;700&display=swap">
<style>
:root{
  --red:#e8262a;
  --red-dark:#c62d2c;
  --red-deep:#b82727;
  --orange:#f7a94b;
  --orange-soft:#f4a35c;
  --bar:#d8492f;
  --ink:#222;
  --grey:#555;
  --line:#e26060;
  --panel:#e6e6e6;
  --white:#fff;
  --room-light:#f3f1ee;
  --room-mid:#e2dcd5;
  --carpet:#d3c8bb;
  --floor:#c49a72;
  --denim:#4f6b96;
  --laptop:#8a8d92;
}
*{box-sizing:border-box;margin:0;padding:0}
html,body{width:976px;height:1200px;overflow:hidden;background:var(--white)}
body{font-family:"Arimo",Arial,sans-serif;color:var(--ink);position:relative}
a{color:inherit;text-decoration:none}

/* header */
.site-header{position:absolute;left:0;top:0;width:976px;height:124px;background:var(--red)}
.utility-bar{position:absolute;left:0;top:0;width:976px;height:22px;background:var(--red-dark);color:var(--white);font-size:10px;line-height:22px}
.utility-bar span{position:absolute;top:0}
.utility-bar .sep{width:1px;height:22px;background:#e05656}
.quote-tab{position:absolute;left:711px;top:23px;width:110px;height:16px;background:var(--red-deep);color:var(--white);font-size:10px;line-height:16px;text-align:center}
.brand{position:absolute;left:139px;top:28px;display:flex;align-items:center}
.brand-mark{width:60px;height:60px;border-radius:50%;background:#d63a30;margin-right:11px}
.brand-name{color:var(--white);font-weight:700;font-size:21px;letter-spacing:.5px;line-height:1}
.brand-sub{color:var(--white);font-weight:700;font-size:7px;letter-spacing:4.4px;margin-top:6px;border-top:1px solid rgba(255,255,255,.8);padding-top:4px}
.social{position:absolute;top:51px;width:27px;height:26px;border-radius:5px;background:var(--white)}
.main-nav{position:absolute;left:154px;top:98px;display:flex;height:26px}
.main-nav a{color:var(--white);font-size:12px;line-height:26px;padding:0 9.5px}
.main-nav a.active{background:var(--white);color:var(--ink);padding:0 7px}

/* slider */
.slider-tabs .tab{position:absolute;top:149px;height:19px;background:var(--red);color:var(--white);font-size:9.5px;line-height:22px;text-align:center;clip-path:polygon(0 0,88% 0,100% 100%,0 100%)}
.slider{position:absolute;left:139px;top:168px;width:683px;height:342px;background:var(--panel)}
.slide-photo{
  position:absolute;left:8px;top:9px;width:499px;height:325px;
  background:
    radial-gradient(ellipse 30% 22% at 48% 88%, rgba(138,141,146,.85), rgba(138,141,146,0) 100%),
    radial-gradient(ellipse 34% 26% at 30% 66%, rgba(79,107,150,.6), rgba(79,107,150,0) 100%),
    radial-gradient(ellipse 22% 28% at 46% 42%, rgba(236,238,242,.9), rgba(236,238,242,0) 100%),
    radial-gradient(ellipse 30% 30% at 88% 88%, rgba(196,154,114,.75), rgba(196,154,114,0) 100%),
    radial-gradient(ellipse 70% 35% at 35% 35%, rgba(255,255,255,.9), rgba(255,255,255,0) 100%),
    linear-gradient(180deg, var(--room-light) 0%, var(--room-mid) 50%, var(--carpet) 80%, #c9bcad 100%);
}
.caption-panel{position:absolute;left:507px;top:9px;width:167px;height:325px}
.caption-active{height:231px;background:var(--red);color:var(--white);padding:8px 8px}
.caption-active h3{font-size:11.5px;font-weight:700;margin-bottom:11px}
.caption-active p{font-family:"Tinos","Times New Roman",serif;font-size:9.6px;line-height:13px;margin-bottom:13px;hyphens:auto}
.caption-active .more{font-family:"Tinos","Times New Roman",serif;font-weight:700;font-size:9.8px}
.caption-row{height:31px;color:var(--white);font-weight:700;font-size:11.5px;line-height:31px;padding-left:8px;background:var(--red-dark);border-top:1px solid #d84040}
.caption-row.hi{background:var(--orange)}

/* service cards */
.service{position:absolute;top:529px;width:129px;height:131px;border:1px solid #ddd;border-radius:4px;box-shadow:0 1px 3px rgba(0,0,0,.15);text-align:center;background:var(--white)}
.service h4{font-weight:400;color:var(--red);font-size:13.5px;margin-top:13px}
.service p{font-size:7.6px;color:var(--grey);line-height:10px;margin-top:5px}
.service .art{width:84px;height:50px;margin:8px auto 0;border-radius:3px}

/* section headings */
.section-title{position:absolute;top:682px;font-size:17px;font-weight:400;color:var(--ink);display:flex;align-items:center}
.section-title::after{content:"";display:block;height:1px;background:var(--line);margin-left:10px}
.blog-title::after{width:284px}
.feat-title::after{width:201px}

/* blog */
.post{position:absolute;left:139px;width:326px;font-size:9.6px;line-height:12px;color:var(--grey)}
.post .avatar{float:left;width:64px;height:65px;background:var(--red);margin:0 10px 0 0;display:flex;align-items:center;justify-content:center}
.post .avatar i{display:block;width:34px;height:34px;border-radius:50%;background:var(--white)}
.post h5{font-size:13.5px;font-weight:400;color:var(--red);line-height:16px}
.post .when{font-size:8.3px;margin:3px 0 9px}
.post p{margin-bottom:11px}
.post .more{display:block;clear:both;text-align:right;color:var(--red);font-size:9.6px;margin-top:-3px}

/* featured projects */
.project{position:absolute;left:483px;width:338px;font-size:9.6px;line-height:11.6px;color:var(--grey)}
.project .thumb{position:absolute;left:0;top:0;width:70px;height:71px;border:2px solid var(--red);background:linear-gradient(180deg,#f4f6fa 0%,#e3e8f0 100%)}
.project .body{margin-left:75px}
.project h5{font-size:13.5px;font-weight:400;color:var(--red);line-height:16px}
.project p{margin-bottom:12px}
.project .more{display:block;text-align:right;color:var(--red);margin-top:-7px}

/* footer */
.site-footer{position:absolute;left:0;top:1008px;width:976px;height:126px;background:linear-gradient(180deg,#e42525 0%,#c93232 100%)}
.footer-col{position:absolute;top:24px;color:var(--white)}
.footer-col h6{font-size:14.5px;font-weight:400;color:var(--orange-soft);margin-bottom:5px}
.footer-col li{list-style:none;font-size:9.6px;line-height:14.6px}
.footer-bar{position:absolute;left:0;top:1134px;width:976px;height:26px;background:var(--bar);display:flex;padding-left:139px}
.footer-bar a{color:#f7c86a;font-size:9.6px;line-height:26px;padding:0 7px;border-left:1px solid #e8735a}
.footer-bar a:first-child{border-left:0;padding-left:0}
.copyright{position:absolute;left:0;top:1165px;width:976px;text-align:center;font-size:9.6px;color:var(--grey)}
</style>
</head>
<body>

<header class="site-header">
  <div class="utility-bar">
    <span style="left:138px">www.CedarlineSurveys.ca</span>
    <span style="left:305px">www.OttawaNimbusStudio.ca</span>
    <span style="left:545px">Contact Us Today</span>
    <span class="sep" style="left:632px"></span>
    <span style="left:639px">555-014-2290</span>
    <span class="sep" style="left:709px"></span>
    <span style="left:716px">sales@brindlecove.ca</span>
  </div>
  <a class="quote-tab" href="#">Request a Quote</a>
  <div class="brand">
    <span class="brand-mark"></span>
    <div>
      <div class="brand-name">BrindleCove</div>
      <div class="brand-sub">COMMUNICATIONS</div>
    </div>
  </div>
  <a class="social" style="left:763px" href="#" aria-label="Social profile"></a>
  <a class="social" style="left:795px" href="#" aria-label="Social profile"></a>
  <nav class="main-nav">
    <a class="active" href="#">Home</a>
    <a href="#">Web Design</a>
    <a href="#">Mobile Apps</a>
    <a href="#">Custom Software</a>
    <a href="#">Accessible PDF/HTML</a>
    <a href="#">CMS: Nimbus/Corvid</a>
    <a href="#">Contact Us</a>
  </nav>
</header>

<div class="slider-tabs">
  <div class="tab" style="left:147px;width:118px">Our Vision</div>
  <div class="tab" style="left:265px;width:118px">Business</div>
  <div class="tab" style="left:384px;width:118px">Government</div>
  <div class="tab" style="left:502px;width:135px">Associations / Non-Profit</div>
</div>

<section class="slider">
  <div class="slide-photo" role="img" aria-label="Photo of a couple relaxing on a rug in a bright living room with a white sofa, browsing on a laptop"></div>
  <div class="caption-panel">
    <div class="caption-active">
      <h3>Caption Title</h3>
      <p>Lorem ipsum dolor sit amet, consectetur adipiscing elit. Nam sit amet dui elit. Curabitur tortor metus, ultrices fermentum feugiat eu, blandit ac ipsum.</p>
      <p>Curabitur vitae arcu purus. Vivamus venenatis iaculis lorem eu scelerisque. In hac habitasse platea dictumst.</p>
      <a class="more" href="#">Learn More</a>
    </div>
    <div class="caption-row">Caption Title</div>
    <div class="caption-row hi">Caption Title</div>
    <div class="caption-row">Caption Title</div>
  </div>
</section>

<section class="services">
  <div class="service" style="left:139px">
    <h4>Web Design</h4>
    <p>Lorem ipsum dolor sit amet,<br>consectetur adipiscing elit.</p>
    <div class="art" role="img" aria-label="Laptop showing a website" style="background:linear-gradient(135deg,#3a4150,#b9c2d0)"></div>
  </div>
  <div class="service" style="left:277px">
    <h4>Mobile Apps</h4>
    <p>Lorem ipsum dolor sit amet,<br>consectetur adipiscing elit.</p>
    <div class="art" role="img" aria-label="Row of smartphones" style="background:linear-gradient(135deg,#222,#6b6f75)"></div>
  </div>
  <div class="service" style="left:416px">
    <h4>Custom Software</h4>
    <p>Lorem ipsum dolor sit amet,<br>consectetur adipiscing elit.</p>
    <div class="art" role="img" aria-label="Laptops running custom software" style="background:linear-gradient(135deg,#d9dde3,#8d96a3)"></div>
  </div>
  <div class="service" style="left:553px">
    <h4>PDF / HTML</h4>
    <p>Lorem ipsum dolor sit amet,<br>consectetur adipiscing elit.</p>
    <div class="art" role="img" aria-label="Document file icons" style="background:linear-gradient(135deg,#9fc46a,#e23a2e)"></div>
  </div>
  <div class="service" style="left:691px">
    <h4>Nimbus / Corvid</h4>
    <p>Lorem ipsum dolor sit amet,<br>consectetur adipiscing elit.</p>
    <div class="art" role="img" aria-label="Content management system icons" style="background:linear-gradient(135deg,#f29a3a,#2a7fc4)"></div>
  </div>
</section>

<h2 class="section-title blog-title" style="left:139px">Blog</h2>
<h2 class="section-title feat-title" style="left:483px">Featured Projects</h2>

<article class="post" style="top:709px">
  <div class="avatar"><i></i></div>
  <h5>Posting Title</h5>
  <div class="when">5hrs, 3 mins ago</div>
  <p>Lorem ipsum dolor sit amet, consectetur adipiscing elit. Nam sit amet dui elit. Curabitur tortor metus, ultrices fermentum feugiat eu, blandit ac ipsum. Curabitur vitae isque. In hac habitasse platea dictumst. Donec semper tellus sit amet orci rhoncus fringilla. Morbi vel mi eu elit accumsan pharetra rutrum id nulla. Fusce tincidunt convallis lectus vel facilisis.</p>
  <a class="more" href="#">Read More</a>
</article>

<article class="post" style="top:845px">
  <div class="avatar"><i></i></div>
  <h5>Posting Title</h5>
  <div class="when">5hrs, 3 mins ago</div>
  <p>Lorem ipsum dolor sit amet, consectetur adipiscing elit. Nam sit amet dui elit. Curabitur tortor metus, ultrices fermentum feugiat eu, blandit ac ipsum. Curabitur vitae isque. In hac habitasse platea dictumst. Donec semper tellus sit amet orci.</p>
  <p>Rhoncus fringilla. Morbi vel mi eu elit accumsan pharetra rutrum id nulla. Fusce tincidunt convallis lectus vel facilisis.</p>
  <a class="more" href="#">Read More</a>
</article>

<article class="project" style="top:711px">
  <div class="thumb" role="img" aria-label="Screenshot of a government website project"></div>
  <div class="body">
    <h5>Project Name</h5>
    <p>Lorem ipsum dolor sit amet, consectetur adipiscing elit. Nam sit amet dui elit. Curabitur tortor metus, ultrices fermentum.</p>
    <p>Habitasse platea dictumst. Donec semper tellus sit amet orci rhoncus fringilla. Morbi vel mi eu elit.</p>
    <a class="more" href="#">View Project</a>
  </div>
</article>

<article class="project" style="top:806px">
  <div class="thumb" role="img" aria-label="Screenshot of a government website project"></div>
  <div class="body">
    <h5>Project Name</h5>
    <p>Lorem ipsum dolor sit amet, consectetur adipiscing elit. Nam sit amet dui elit. Curabitur tortor metus, ultrices fermentum.</p>
    <p>Habitasse platea dictumst. Donec semper tellus sit amet orci rhoncus fringilla. Morbi vel mi eu elit.</p>
    <a class="more" href="#">View Project</a>
  </div>
</article>

<article class="project" style="top:900px">
  <div class="thumb" role="img" aria-label="Screenshot of a government website project"></div>
  <div class="body">
    <h5>Project Name</h5>
    <p>Lorem ipsum dolor sit amet, consectetur adipiscing elit. Nam sit amet dui elit. Curabitur tortor metus, ultrices fermentum.</p>
    <p>Habitasse platea dictumst. Donec semper tellus sit amet orci rhoncus fringilla. Morbi vel mi eu elit.</p>
    <a class="more" href="#">View Project</a>
  </div>
</article>

<footer>
  <div class="site-footer">
    <div class="footer-col" style="left:139px"><h6>Web Design</h6><ul><li>Item One</li><li>Item Two</li><li>Item Three</li><li>Item Four</li></ul></div>
    <div class="footer-col" style="left:311px"><h6>Mobile Aps</h6><ul><li>Item One</li><li>Item Two</li><li>Item Three</li><li>Item Four</li></ul></div>
    <div class="footer-col" style="left:484px"><h6>PDF / HTML</h6><ul><li>Item One</li><li>Item Two</li><li>Item Three</li><li>Item Four</li></ul></div>
    <div class="footer-col" style="left:657px"><h6>Nimbus / Corvid</h6><ul><li>Item One</li><li>Item Two</li><li>Item Three</li><li>Item Four</li></ul></div>
  </div>
  <nav class="footer-bar">
    <a href="#">Site Map</a>
    <a href="#">Home</a>
    <a href="#">Web Design</a>
    <a href="#">Mobile Apps</a>
    <a href="#">Accessible PDF/HTML</a>
    <a href="#">CMS: Nimbus/Corvid</a>
  </nav>
  <p class="copyright">Copyright © 2011 -BrindleCove Communications - 42 Larkspur Lane, Ottawa, ON, K1Z 0X9 (555) 014-2290</p>
</footer>

</body>
</html>
```